BrixaPlay Business Card

We need a business card design for our company. We sell construction-themed amusement rides for kids.

Contact Information for Business Card

Contact info on business card should include:
Rick Dunmore
Co-Founder & COO
(833) 512-BRIXAPL
Rick@brixaplay.example
www.brixaplay.example

```html
<!DOCTYPE html>
<html lang="en">
<head>
<meta charset="utf-8">
<title>BrixaPlay Business Card</title>
<link rel="stylesheet" href="https://fonts.googleapis.com/css2?family=Arimo:wght@400;700&display=swap">
<style>
  :root {
    --bg: #e9e9e9;
    --card: #000000;
    --orange: #f07a2a;
    --white: #ffffff;
    --rule: #6a6a6a;
  }
  * { box-sizing: border-box; margin: 0; padding: 0; }
  html, body {
    width: 1200px; height: 801px; overflow: hidden;
    background: var(--bg);
    font-family: "Arimo", Arial, sans-serif;
  }
  .sheet {
    width: 1200px; height: 801px;
    display: flex; align-items: center; justify-content: center; gap: 50px;
  }
  .card {
    width: 540px; height: 309px;
    background: var(--card);
    border-bottom: 3px solid var(--orange);
    border-right: 3px solid var(--orange);
    box-shadow: 0 10px 24px rgba(0,0,0,.25);
    position: relative;
    color: var(--white);
  }
  .brand {
    display: flex; align-items: center; gap: 10px;
    color: var(--orange); font-weight: 700;
  }
  .brand-dot {
    border-radius: 50%; background: var(--orange); flex: none;
  }
  /* front side */
  .card-front { display: flex; align-items: center; }
  .card-front .brand-zone {
    width: 270px; display: flex; justify-content: center;
  }
  .card-front .brand { font-size: 34px; }
  .card-front .brand-dot { width: 14px; height: 14px; }
  .divider {
    width: 1px; height: 140px; background: var(--rule);
  }
  .contact { padding-left: 26px; }
  .contact-name { color: var(--orange); font-weight: 700; font-size: 19px; }
  .contact-role { font-size: 14px; margin-top: 4px; }
  .contact-list { list-style: none; margin-top: 18px; }
  .contact-list li {
    display: flex; align-items: center; gap: 10px;
    font-size: 13px; margin-bottom: 7px;
  }
  .contact-list svg { width: 12px; height: 12px; flex: none; }
  .accent { color: var(--orange); }
  /* back side */
  .card-back { display: flex; align-items: center; justify-content: center; }
  .card-back .brand { font-size: 52px; gap: 14px; }
  .card-back .brand-dot { width: 20px; height: 20px; }
</style>
</head>
<body>
<main class="sheet">
  <section class="card card-front" aria-label="Card front">
    <div class="brand-zone">
      <div class="brand"><span class="brand-dot"></span>BrixaPlay</div>
    </div>
    <div class="divider"></div>
    <div class="contact">
      <p class="contact-name">Rick Dunmore</p>
      <p class="contact-role">Co-Founder &amp; COO</p>
      <ul class="contact-list">
        <li>
          <svg viewBox="0 0 12 12" aria-hidden="true"><path d="M3 1 L5 3.5 L4 5 Q5.5 7 7 8 L8.5 7 L11 9 L9.5 11 Q4 10 1 2.5 Z" fill="var(--orange)"/></svg>
          (833) 512-BRIXAPL
        </li>
        <li>
          <svg viewBox="0 0 12 12" aria-hidden="true"><rect x="1" y="2.5" width="10" height="7" fill="none" stroke="var(--orange)" stroke-width="1.3"/><path d="M1 2.5 L6 6.5 L11 2.5" fill="none" stroke="var(--orange)" stroke-width="1.3"/></svg>
          Rick@brixaplay.example
        </li>
        <li>
          <svg viewBox="0 0 12 12" aria-hidden="true"><circle cx="6" cy="6" r="5.5" fill="var(--orange)"/><path d="M0.5 6 H11.5 M6 0.5 V11.5" stroke="var(--card)" stroke-width=".8"/></svg>
          <span>www.<span class="accent">brixaplay</span>.example</span>
        </li>
      </ul>
    </div>
  </section>

  <section class="card card-back" aria-label="Card back">
    <div class="brand"><span class="brand-dot"></span>BrixaPlay</div>
  </section>
</main>
</body>
</html>
```